Athletic Director Business Card

I need a business card that is very appealing and shows my school logo and colours (red, white and black). We just finished changing our school logo and have sent the two logos we use and I have also sent the logo W that we also use. I'm not sure if combining them works but I thought I would send it anyway and let your creative juices flow. Looking for a simple but very luring design. It could have the different sports on it but I think doing something with the logo is probably the direction I would like to see as we offer 11 different sports and 22 different teams so that might get to busy. We have a long "Tradition of Excellence" and maybe that could be on the card. If you need to change to logo by shadowing it, or making it a two colour with a glow in it or what every you think would make it look fantastic give it a try as I'm open to different looks.

Target Market(s)

Parents of high school athletes, businesses throughout our city, principals.

Industry/Entity Type

School

Requirements
Must have
• Name of School - Ridgemont Valley High School or just Ridgemont Valley.
My Name - Darren Whitfield
Position - Athletic Director
Phone - 403-555-0147
Cell - 403-555-0183
Email - dwhitfield@pvsd.ab.ca
Website - www.ridgemontvalleyathletics.com

```html
<!DOCTYPE html>
<html lang="en">
<head>
<meta charset="utf-8">
<title>Darren Whitfield – Athletic Director Business Card</title>
<link href="https://fonts.googleapis.com/css2?family=Open+Sans:wght@400;600;700&display=swap" rel="stylesheet">
<style>
  :root {
    --page-bg: #e9e6e1;
    --card-white: #fafafa;
    --ink-dark: #3a3a3a;
    --ink-mid: #555555;
    --brand-red: #d3202f;
    --band-dark: #2a2a2a;
    --back-black: #111111;
    --divider: #c9c9c9;
    --tagline: #eeeeee;
  }
  * { box-sizing: border-box; margin: 0; padding: 0; }
  html, body {
    width: 1200px; height: 1023px; overflow: hidden;
    background: var(--page-bg);
    font-family: "Open Sans", Arial, sans-serif;
  }
  .sheet {
    width: 1200px; height: 1023px;
    display: flex; align-items: center; justify-content: center; gap: 60px;
  }
  .card {
    position: relative; border-radius: 4px; overflow: hidden;
    box-shadow: 0 10px 30px rgba(0,0,0,0.18);
  }

  /* Front */
  .card-front { width: 640px; height: 366px; background: var(--card-white); }
  .team-mark {
    position: absolute; left: 36px; top: 0; width: 220px; height: 332px;
    display: flex; align-items: center; gap: 10px;
  }
  .team-mark__dot {
    width: 26px; height: 26px; border-radius: 50%;
    background: var(--brand-red); flex: none;
  }
  .team-mark__name {
    font-size: 24px; font-weight: 700; color: var(--ink-dark); line-height: 1.2;
  }
  .divider {
    position: absolute; left: 272px; top: 36px; width: 1px; height: 250px;
    background: var(--divider);
  }
  .person { position: absolute; left: 300px; top: 40px; }
  .person__name { font-size: 20px; font-weight: 400; color: var(--ink-mid); line-height: 1.3; }
  .person__title { font-size: 14px; color: var(--brand-red); margin-top: 2px; }
  .contacts {
    position: absolute; left: 310px; top: 140px; list-style: none;
    display: flex; flex-direction: column; gap: 10px;
  }
  .contacts li {
    display: flex; align-items: center; gap: 10px;
    font-size: 14px; line-height: 1.4; color: var(--ink-dark); white-space: nowrap;
  }
  .contacts svg { width: 17px; height: 17px; fill: var(--brand-red); flex: none; }
  .band {
    position: absolute; left: 0; right: 0; bottom: 0; height: 34px; display: flex;
  }
  .band__school {
    width: 290px; background: var(--band-dark); color: #eeeeee;
    font-size: 15px; font-weight: 600; letter-spacing: 2px;
    display: flex; align-items: center; padding-left: 36px;
  }
  .band__accent { flex: 1; background: var(--brand-red); }

  /* Back */
  .card-back {
    width: 366px; height: 640px;
    background: radial-gradient(ellipse at 60% 30%, #262626 0%, var(--back-black) 70%);
  }
  .back-mark {
    position: absolute; left: 0; right: 0; top: 40px;
    display: flex; justify-content: center; align-items: center; gap: 10px;
  }
  .back-mark__square { width: 20px; height: 20px; background: var(--brand-red); flex: none; }
  .back-mark__name { font-size: 22px; font-weight: 700; color: var(--brand-red); white-space: nowrap; }
  .back-emblem {
    position: absolute; left: 60px; top: 150px; width: 260px; height: 300px;
    border-radius: 40%;
    background: radial-gradient(ellipse at 50% 45%, rgba(150,24,34,0.35) 0%, rgba(60,20,22,0.25) 55%, rgba(17,17,17,0) 75%);
  }
  .tagline {
    position: absolute; left: 34px; top: 360px;
    transform-origin: left top; transform: rotate(90deg) translateY(-100%);
    font-size: 24px; font-weight: 400; color: var(--tagline);
    letter-spacing: 0.5px; white-space: nowrap;
  }
</style>
</head>
<body>
<main class="sheet">

  <section class="card card-front" aria-label="Business card front">
    <div class="team-mark">
      <span class="team-mark__dot"></span>
      <span class="team-mark__name">Valley<br>Kestrels</span>
    </div>
    <div class="divider"></div>
    <div class="person">
      <p class="person__name">Darren Whitfield</p>
      <p class="person__title">Athletic Director</p>
    </div>
    <ul class="contacts">
      <li>
        <svg viewBox="0 0 24 24" aria-hidden="true"><path d="M6.6 10.8a15.1 15.1 0 0 0 6.6 6.6l2.2-2.2c.3-.3.7-.4 1-.2 1.1.4 2.3.6 3.6.6.6 0 1 .4 1 1V20c0 .6-.4 1-1 1A17 17 0 0 1 3 4c0-.6.4-1 1-1h3.5c.6 0 1 .4 1 1 0 1.3.2 2.5.6 3.6.1.3 0 .7-.2 1z"/></svg>
        403-555-0147
      </li>
      <li>
        <svg viewBox="0 0 24 24" aria-hidden="true"><path d="M7 1h10a2 2 0 0 1 2 2v18a2 2 0 0 1-2 2H7a2 2 0 0 1-2-2V3a2 2 0 0 1 2-2zm0 3v14h10V4zm5 15.5a1 1 0 1 0 0 2 1 1 0 0 0 0-2z"/></svg>
        403-555-0183
      </li>
      <li>
        <svg viewBox="0 0 24 24" aria-hidden="true"><path d="M3 5h18a1 1 0 0 1 1 1v12a1 1 0 0 1-1 1H3a1 1 0 0 1-1-1V6a1 1 0 0 1 1-1zm1 2.3V17h16V7.3l-8 5.2z M4.5 7l7.5 4.8L19.5 7z"/></svg>
        dwhitfield@pvsd.ab.ca
      </li>
      <li>
        <svg viewBox="0 0 24 24" aria-hidden="true"><path d="M12 2a10 10 0 1 0 0 20 10 10 0 0 0 0-20zm6.9 9h-3a15 15 0 0 0-1.3-5.6A8 8 0 0 1 18.9 11zM12 4.1c.9 1.2 1.8 3.6 1.9 6.9h-3.8c.1-3.3 1-5.7 1.9-6.9zM9.4 5.4A15 15 0 0 0 8.1 11h-3a8 8 0 0 1 4.3-5.6zM5.1 13h3a15 15 0 0 0 1.3 5.6A8 8 0 0 1 5.1 13zm6.9 6.9c-.9-1.2-1.8-3.6-1.9-6.9h3.8c-.1 3.3-1 5.7-1.9 6.9zm2.6-1.3a15 15 0 0 0 1.3-5.6h3a8 8 0 0 1-4.3 5.6z"/></svg>
        www.ridgemontvalleyathletics.com
      </li>
    </ul>
    <div class="band">
      <div class="band__school">Ridgemont Valley</div>
      <div class="band__accent"></div>
    </div>
  </section>

  <section class="card card-back" aria-label="Business card back">
    <div class="back-mark">
      <span class="back-mark__square"></span>
      <span class="back-mark__name">Ridgemont Valley</span>
    </div>
    <div class="back-emblem" role="img" aria-label="Faint oversized team mascot emblem in dark red"></div>
    <p class="tagline">Tradition of Excellence</p>
  </section>

</main>
</body>
</html>
```